Create a Brochure Design for Brantley Homecare

Brantley Homecare is a subsidiary of the Brantley Care Group. This brochure is specifically for the Brantley Homecare company and brand. Create a 3 panel, A4, front and back, tri-fold brochure. This brochure will be a way to introduce our Homecare services to the community, prospective clients, and various referral partners. The brochure must be eye catching, unique in its deliverables and demonstrate both attention to detail and comfort. Our organization is sophisticated and built around warmth, care and individualized personal attention. The most important aspect of this design is to focus on creating a nurturing, warm, and inviting feel where you would want to have a Nurse or Nurse’s Aide in your own home or a loved one’s home.

I am open to the creativity of the designer to develop something based on the above criteria; however I would like the design to work well with the existing collateral material. What I mean by that is that while I want everything to have its own personality and stand out as its own brand representative, I still need to be able to tell that the overall design concept stays stylistically inside of the same ‘family’ of existing designed material. Because of this, below I would like for the designer to pull inspiration from the link to our website (Located below) as well as from the attachment of our recently refreshed business cards (Attached). This should allow each design to be unique and creative, while still staying inside of a framework and the feel/style that I am looking for.

Finally, I want all the designers to understand that this brochure design is for a private, in home, healthcare company where we are responsible for providing personalized care for a culturally and ethnically diverse make-up clientele of all ages. The photos that are used must represent an image of warmth, care, and a positive interaction between client and caregiver.

Look under the Brantley Homecare tab at www.brantleycaregroup-example.net

Industry/Entity Type

Healthcare

Requirements
Must have
• • The Brantley Homecare company logo must be included.

```html
<!DOCTYPE html>
<html lang="en">
<head>
<meta charset="utf-8">
<title>Brantley Homecare – Tri-fold Brochure</title>
<link rel="stylesheet" href="https://fonts.googleapis.com/css2?family=Tinos:ital,wght@0,400;0,700;1,400&family=Archivo+Narrow:wght@400&family=Open+Sans:wght@700&display=swap">
<style>
  :root{
    --pink:#f4868b;
    --pink-light:#f9aeb1;
    --pink-pale:#fbd2d3;
    --green:#138446;
    --teal:#1f6a5a;
    --white:#ffffff;
    --grey-light:#f2f2f2;
    --grey-mid:#dcdcdc;
    --ink-green:#0f7a3e;
  }
  *{box-sizing:border-box;margin:0;padding:0}
  html,body{width:1200px;height:849px;overflow:hidden;background:#fff}
  .brochure{position:relative;width:1200px;height:849px;overflow:hidden;font-family:"Tinos",serif;color:var(--white)}
  .photo{position:absolute}
  .abs{position:absolute}

  /* Left panel */
  .panel-left{position:absolute;left:0;top:0;width:400px;height:849px;background:var(--white)}
  .left-hero{left:4px;top:4px;width:393px;height:157px;background:linear-gradient(120deg,#c8a58a 0%,#e8c6b4 40%,#b45aa8 75%,#5b3a3a 100%)}
  .left-hero-caption{left:16px;top:88px;font:700 15px/16px "Tinos",serif;color:var(--white);text-shadow:0 1px 2px rgba(0,0,0,.5)}
  .services-intro{left:0;top:158px;width:400px;height:114px;background:var(--pink-light)}
  .services-title{left:20px;top:140px;font:400 19px/1 "Tinos",serif;letter-spacing:2px;color:var(--white)}
  .services-intro p{position:absolute;left:14px;top:7px;width:382px;font:400 16px/17px "Tinos",serif;letter-spacing:1.3px}
  .services-body{left:0;top:272px;width:400px;height:491px;background:var(--pink)}
  .services-body p{position:absolute;left:14px;width:380px;font:400 16px/17px "Tinos",serif;letter-spacing:1.3px}
  .services-body .term{color:var(--teal)}
  .thumbs{left:0;top:768px;width:400px;height:76px;display:flex;gap:4px;padding-left:2px}
  .thumb{flex:1;height:76px}
  .thumb-1{background:linear-gradient(90deg,#b98c74,#efe3d6)}
  .thumb-2{background:linear-gradient(90deg,#9bb08f,#d8c7ae)}
  .thumb-3{background:linear-gradient(90deg,#c9a385,#f3ece6)}
  .left-rule{left:0;top:845px;width:400px;height:4px;background:var(--pink)}

  /* Middle panel */
  .panel-mid{position:absolute;left:400px;top:0;width:400px;height:849px;background:linear-gradient(160deg,var(--grey-mid) 0%,var(--grey-light) 35%,#fafafa 70%,#ececec 100%)}
  .mid-bg{left:0;top:272px;width:400px;height:577px;background:radial-gradient(ellipse at 40% 25%,#d9d9d9 0%,rgba(240,240,240,0) 65%)}
  .mid-hero{left:6px;top:4px;width:390px;height:262px;background:linear-gradient(135deg,#f7e6e6 0%,#d9a897 45%,#b7785e 70%,#f4d4d4 100%)}
  .mid-hero-caption{left:22px;top:162px;font:700 37px/36px "Open Sans",sans-serif;color:var(--white);text-shadow:0 2px 4px rgba(0,0,0,.25)}
  .mid-hero-caption .big{font-size:54px;line-height:52px;display:block}
  .brand{position:absolute;text-align:center;color:var(--green)}
  .brand-mark{display:block;margin:0 auto 14px;background:var(--pink);border-radius:10px}
  .brand-name{font:400 46px/1 "Tinos",serif;color:var(--green);letter-spacing:1px}
  .brand-tag{font:italic 400 15px/17px "Tinos",serif;color:var(--green);margin-top:18px}
  .brand-mid{left:0;top:324px;width:400px}
  .brand-mid .brand-mark{width:76px;height:80px}
  .contact{left:0;top:614px;width:400px;text-align:center;font:400 19px/1 "Archivo Narrow",sans-serif;letter-spacing:2px;color:var(--ink-green)}
  .contact li{list-style:none;height:37px}
  .contact li:first-child{height:29px}

  /* Right panel */
  .panel-right{position:absolute;left:800px;top:0;width:400px;height:849px;background:var(--white)}
  .right-band{left:0;top:0;width:400px;height:270px;background:var(--pink)}
  .right-band .kicker{position:absolute;left:4px;top:116px;font:400 22px/1 "Tinos",serif;letter-spacing:3.2px}
  .right-band .ghost{position:absolute;left:2px;top:142px;font:400 53px/1 "Tinos",serif;letter-spacing:1px;color:rgba(255,255,255,.22);white-space:nowrap}
  .right-band .title{position:absolute;left:2px;top:200px;font:400 53px/1 "Tinos",serif;letter-spacing:1px;white-space:nowrap}
  .right-band .fade{position:absolute;left:0;top:176px;width:400px;height:94px;background:rgba(255,255,255,.18)}
  .brand-right{left:0;top:282px;width:400px}
  .brand-right .brand-mark{width:96px;height:102px}
  .brand-right .brand-name{font-size:56px}
  .brand-right .brand-tag{font-size:19px;line-height:20px;margin-top:16px}
  .right-hero{left:0;top:586px;width:400px;height:263px;background:linear-gradient(110deg,#f3ebe6 0%,#d7b5a3 35%,#8c5d4b 55%,#e9dfe2 80%,#c79a86 100%)}
  .right-hero-caption{left:18px;top:745px;font:700 32px/34px "Open Sans",sans-serif;color:var(--white);text-shadow:0 2px 4px rgba(0,0,0,.3)}
  .right-hero-caption .big{font-size:52px;line-height:48px;display:block}
</style>
</head>
<body>
<main class="brochure">

  <section class="panel-left">
    <div class="photo left-hero abs" role="img" aria-label="Nurse with stethoscope smiling at a young child"></div>
    <p class="left-hero-caption abs">Quality homecare services.<br>The Brantley Way</p>

    <div class="services-intro abs">
      <p>Brantley Homecare provides two different levels of care. Our Nurse Care Consultant will assist the client and family in determining the appropriate level of care needed during the complimentary initial consultation.</p>
    </div>
    <h2 class="services-title abs">Services</h2>

    <div class="services-body abs">
      <p style="top:14px"><span class="term">Nurse Aide Care</span> – Our Nurse Aides help you with your personal care needs, provide companionship, run errands, and do light housekeeping, along with assisting you with the activities of daily living.</p>
      <p style="top:131px"><span class="term">Skilled Nursing Care</span> – We offer a wide range of skilled nursing services using RN’s and LPN’s who provide treatment from wound care to life support, in addition to all of the services performed by our Nurse Aides.</p>
      <p style="top:241px;left:11px">Clients who already receive personal care services can also have the following additional support services.</p>
      <p style="top:304px"><span class="term">Medication Services</span> – Our licensed nurse will pre-pour your medication in weekly pill containers for a 28-day period.</p>
      <p style="top:372px"><span class="term">Transportation Services</span> – Our Care Professionals run errands or escort you to the grocery store, your personal appointments (physician, beautician, therapy), or other outings.</p>
    </div>

    <div class="thumbs abs">
      <div class="thumb thumb-1" role="img" aria-label="Caregiver sitting with an elderly woman"></div>
      <div class="thumb thumb-2" role="img" aria-label="Caregiver helping an older couple at a table"></div>
      <div class="thumb thumb-3" role="img" aria-label="Nurse assisting a senior client at home"></div>
    </div>
    <div class="left-rule abs"></div>
  </section>

  <section class="panel-mid">
    <div class="mid-bg abs" role="img" aria-label="Faint image of clasped hands"></div>
    <div class="photo mid-hero abs" role="img" aria-label="Young hand holding an elderly hand"></div>
    <p class="mid-hero-caption abs">Dependable<span class="big">care</span></p>

    <div class="brand brand-mid">
      <span class="brand-mark"></span>
      <div class="brand-name">Brantley Homecare</div>
      <p class="brand-tag">Someone you can depend on...<br>Without question.</p>
    </div>

    <ul class="contact abs">
      <li>480 Palmcrest Ave, Suite 210</li>
      <li>Lakeview, HI 96700</li>
      <li>phone:(555)010-2486</li>
      <li>Fax:&nbsp;&nbsp;&nbsp;&nbsp;(555)010-2822</li>
      <li>hello@brantleycare-example.com</li>
      <li>www.brantleycare-example.com</li>
    </ul>
  </section>

  <section class="panel-right">
    <div class="right-band abs">
      <div class="fade"></div>
      <p class="kicker">Quality homecare services</p>
      <p class="ghost" aria-hidden="true">The Brantley Way</p>
      <h1 class="title">The Brantley Way</h1>
    </div>

    <div class="brand brand-right">
      <span class="brand-mark"></span>
      <div class="brand-name">Brantley Homecare</div>
      <p class="brand-tag">Someone you can depend on...<br>Without question.</p>
    </div>

    <div class="photo right-hero abs" role="img" aria-label="Smiling senior woman with two caregivers"></div>
    <p class="right-hero-caption abs">Someone you can<span class="big">trust</span></p>
  </section>

</main>
</body>
</html>
```